Real Estate Investing company needs a business card design

We need a business card design for new Real Estate Investment Company called "Maple Ridge Ventures, LLC." We buy homes for cash and close quickly in any situation. Our company provides an easy and fast option for home owners who are in tough situations who need to sell their home fast and don't want realtor fees or other listing hassles. We also renovate and resell our homes which helps provide housing for the community. We would like to see designs that use the colors blue and white to match our company logo or other colors that may match our company logo. The final design should communicate trust and easy process.
Industry/Entity Type
Business
Contact Information for Business Card
Front should have company name and company logo. back of card should have company logo and area to list services.
Look and feel

```html
<!DOCTYPE html>
<html lang="en">
<head>
<meta charset="utf-8">
<title>Maple Ridge Ventures – Business Card</title>
<link rel="stylesheet" href="https://fonts.googleapis.com/css2?family=Open+Sans:wght@400;600;700&display=swap">
<style>
  :root {
    --navy: #1d4fa0;
    --blue: #1a73bd;
    --blue-light: #3d94cf;
    --white: #ffffff;
    --ink: #1b66b3;
    --backdrop: #eef1f5;
  }
  html, body {
    margin: 0;
    padding: 0;
    width: 1200px;
    height: 902px;
    overflow: hidden;
    background: var(--backdrop);
  }
  .stage {
    width: 1200px;
    height: 902px;
    display: flex;
    align-items: center;
    justify-content: center;
  }
  .business-card {
    width: 840px;
    height: 480px;
    filter: drop-shadow(0 8px 18px rgba(20, 40, 80, 0.18));
  }
  .band-navy { fill: var(--navy); }
  .band-white { fill: var(--white); }
  .card-face { fill: var(--white); }
  .company-name {
    font-family: "Open Sans", sans-serif;
    font-weight: 700;
    font-size: 34px;
    fill: var(--white);
    letter-spacing: 0.5px;
  }
  .person-name {
    font-family: "Open Sans", sans-serif;
    font-weight: 700;
    font-size: 34px;
    fill: var(--ink);
  }
  .person-role {
    font-family: "Open Sans", sans-serif;
    font-weight: 600;
    font-size: 22px;
    fill: var(--ink);
  }
  .contact-line {
    font-family: "Open Sans", sans-serif;
    font-weight: 400;
    font-size: 21px;
    fill: var(--ink);
  }
</style>
</head>
<body>
<main class="stage">
  <svg class="business-card" viewBox="0 0 840 480" xmlns="http://www.w3.org/2000/svg" aria-label="Maple Ridge Ventures business card">
    <defs>
      <linearGradient id="panel-gradient" x1="0" y1="1" x2="1" y2="0">
        <stop offset="0" stop-color="var(--blue-light)"/>
        <stop offset="0.55" stop-color="var(--blue)"/>
        <stop offset="1" stop-color="var(--blue)"/>
      </linearGradient>
      <clipPath id="card-shape">
        <rect x="0" y="0" width="840" height="480" rx="18"/>
      </clipPath>
    </defs>

    <g clip-path="url(#card-shape)">
      <rect class="card-face" x="0" y="0" width="840" height="480"/>

      <!-- brand panel -->
      <polygon class="brand-panel" points="0,34 390,34 560,446 0,446" fill="url(#panel-gradient)"/>

      <!-- top bands -->
      <rect class="band-navy" x="0" y="0" width="840" height="20"/>
      <rect class="band-white" x="0" y="20" width="840" height="8"/>
      <rect class="band-navy" x="0" y="28" width="840" height="6"/>

      <!-- bottom bands -->
      <rect class="band-navy" x="0" y="446" width="840" height="6"/>
      <rect class="band-white" x="0" y="452" width="840" height="8"/>
      <rect class="band-navy" x="0" y="460" width="840" height="20"/>
    </g>

    <!-- company name in place of the mark -->
    <g class="brand-lockup">
      <rect x="60" y="214" width="22" height="22" fill="var(--white)"/>
      <text class="company-name" x="96" y="236">Maple Ridge</text>
      <text class="company-name" x="96" y="276">Ventures</text>
    </g>

    <!-- contact details -->
    <g class="contact-block">
      <text class="person-name" x="560" y="108">John Doe</text>
      <text class="person-role" x="600" y="136">position</text>
      <text class="contact-line" x="560" y="214">address</text>
      <text class="contact-line" x="560" y="250">phone number</text>
      <text class="contact-line" x="560" y="286">e-mail</text>
    </g>
  </svg>
</main>
</body>
</html>
```